Ecommerce brand for entrepreneurs needs help with branding products

I am looking for help to design a small supplement pouch. Including colours, layout and design.

The business:
The business is called 'Tall Ember' and our goal is to help entrepreneurs continue to change the world in spite of how difficult it is.

At Tall Ember, we understand being an entrepreneur is one of the hardest jobs there is. We believe there is a better way. A way in which you don’t have to choose between success in your business and the rest of your life. Our aim is to solve these challenges, so you can stay in the fight a little longer. If we can do this, we can ultimately change the world into a better place.

We will do this through a range of supplements, community, information and physical products to help you optimise their lives.

The product:
The product I am looking to create is for a natural nootropic called

‘The Quiet Lantern’

The product will address the challenges with focus and lower attention spans.

So Entrepreneurs can Solve more problems, Help more people and make more money.

Do more in four hours than a whole day. Have Zen like calm. With Zero Jitters & Zero Crashes. Do what others can’t

The design:
I want this to be a small pouch. The final design should be elegant, and minimalist and have an edge that is different.

I have added examples of products that I like below.

I am open to most colour combinations but silver, navy, black, orange, white and translucent are what is taking my fancy right now.

I like the idea of having a translucent package or part of the package like some of the designs below. I also like the matt finish of some of the designs along with the flashes of shininess from silver for contrast. or even using embossing within the packaging.

I have a logo that I have made but I am open to changes on that as well if you see fit. if you do want to do this, I would love to see an emblem next to the words Tall Ember that encapsulates the brand.

I have done some really really rough mockups myself but would like to see what you have to offer rather than what I have done

The purpose of this image:
I need a 3D mockup of this supplement to be on my landing page to start to take pre-orders.

I am ideally looking for 2 images

1) Supplement packaging on its own
2) Supplement packaging with background coloured lighting, with powder on the ground etc

Need extra days to review

The logo: Please also redesign my logo - I would love to see an emblem next to the words Tall Ember that encapsulates the brand.The business is called 'Tall Ember' and our goal is to help entrepreneurs continue to change the world in spite of how difficult it is. At Tall Ember, we understand being an entrepreneur is one of the hardest jobs there is. We believe there is a better way. A way in which you don’t have to choose between success in your business and the rest of your life. Our aim is to solve these challenges, so you can stay in the fight a little longer. If we can do this, we can ultimately change the world into a better place. We will do this through a range of supplements, community, information and physical products to help you optimise their lives.

Supplements for entrepreneurs

• The design: I want this to be a small pouch. The final design should be elegant, and minimalist and have an edge that is different. I have added examples of products that I like below. I am open to most colour combinations but silver, navy, black, orange, white and translucent are what is taking my fancy right now. I like the idea of having a translucent package or part of the package like some of the designs below. I also like the matt finish of some of the designs along with the flashes of shininess from silver for contrast. or even using embossing within the packaging.

```html
<!DOCTYPE html>
<html lang="en">
<head>
<meta charset="utf-8">
<title>The Quiet Lantern – Tall Ember pouch</title>
<link href="https://fonts.googleapis.com/css2?family=Montserrat:wght@400;500;700;800&display=swap" rel="stylesheet">
<style>
  :root {
    --backdrop: #f6bf2e;
    --pouch: #121212;
    --pouch-edge: #1e1e1e;
    --accent-red: #e8402a;
    --ink-white: #f4f4f4;
    --ink-grey: #b9b9b9;
    --smoke-light: rgba(200, 200, 200, 0.32);
    --smoke-dark: rgba(60, 60, 60, 0.0);
  }
  html, body {
    margin: 0;
    padding: 0;
    width: 1200px;
    height: 852px;
    overflow: hidden;
    background: var(--backdrop);
    font-family: "Montserrat", Arial, sans-serif;
  }
  .canvas {
    position: relative;
    width: 1200px;
    height: 852px;
  }
  .pouch {
    position: absolute;
    left: 330px;
    top: 38px;
    width: 540px;
    height: 776px;
    background: linear-gradient(160deg, var(--pouch-edge) 0%, var(--pouch) 45%, #0b0b0b 100%);
    border-radius: 22px;
    overflow: hidden;
  }
  .zip-line {
    position: absolute;
    left: 0;
    right: 0;
    top: 58px;
    height: 1px;
    background: rgba(255, 255, 255, 0.08);
  }
  .hero-visual {
    position: absolute;
    left: 30px;
    top: 80px;
    width: 260px;
    height: 620px;
    background:
      radial-gradient(ellipse 40% 30% at 55% 30%, var(--smoke-light), var(--smoke-dark) 70%),
      radial-gradient(ellipse 35% 40% at 45% 70%, rgba(170,170,170,0.22), var(--smoke-dark) 70%);
  }
  .product-name {
    position: absolute;
    left: 24px;
    bottom: 150px;
    margin: 0;
    writing-mode: vertical-rl;
    transform: rotate(180deg);
    color: var(--accent-red);
    font-weight: 500;
    font-size: 92px;
    line-height: 0.95;
    letter-spacing: -1px;
  }
  .headline {
    position: absolute;
    left: 270px;
    top: 236px;
    margin: 0;
    color: var(--ink-white);
    font-weight: 800;
    font-size: 21px;
    line-height: 1.75;
    letter-spacing: 0.5px;
    text-transform: uppercase;
  }
  .details {
    position: absolute;
    left: 270px;
    top: 512px;
    width: 240px;
    margin: 0;
    color: var(--ink-grey);
    font-size: 8.5px;
    line-height: 1.5;
    text-transform: uppercase;
    letter-spacing: 0.3px;
  }
  .brand {
    position: absolute;
    left: 32px;
    bottom: 36px;
    margin: 0;
    display: flex;
    align-items: center;
    gap: 10px;
    color: var(--ink-white);
    font-weight: 500;
    font-size: 22px;
    line-height: 1;
  }
  .brand-dot {
    width: 12px;
    height: 12px;
    border-radius: 50%;
    background: var(--ink-white);
  }
  .net-weight {
    position: absolute;
    right: 26px;
    bottom: 36px;
    margin: 0;
    color: var(--accent-red);
    font-size: 15px;
    font-weight: 500;
  }
</style>
</head>
<body>
<main class="canvas">
  <section class="pouch">
    <div class="zip-line"></div>
    <div class="hero-visual" role="img" aria-label="Soft smoky monochrome photograph of a figure"></div>
    <h1 class="product-name">Quiet<br>Lantern</h1>
    <p class="headline">Challenge your<br>low attention<br>span<br>and focus</p>
    <p class="details">Natural nootropic blend for calm, steady focus. Zero jitters, zero crashes. Take one scoop with water each morning. Store in a cool, dry place. Not for children.</p>
    <p class="brand"><span class="brand-dot"></span>Tall Ember</p>
    <p class="net-weight">Net wt. 300 gm</p>
  </section>
</main>
</body>
</html>
```